New Family Dental Office Needs a Brochure Design

We need a brochure design for a new family dental office in Edmonton, Alberta Canada called Maple Grin Family Dental. We would like to see a design that ties in with our office colours and website design. It should communicate a modern feel and introduce our office and our staff and well as the services we offer. Our website is www.maplegrin.ca and our Twitter @MapleGrinDTX
Trifold brochure

Target Market(s)

New patients

Industry/Entity Type

Dental

Font styles to use
Sans Serif

Colors
9bcb3c
0355a3
959595

Requirements
Must have
• Overwiew of the practice
• Meet the doctors
• Services offered
• Map of location on the back
• Photos of the 2 dentists
• The logo and color scheme as seen on the website
• Must tie in with the website
Nice to have
• Some photos or schematics of the procedures.

```html
<!DOCTYPE html>
<html lang="en">
<head>
<meta charset="utf-8">
<title>Maple Grin Family Dental – Trifold Brochure</title>
<link rel="stylesheet" href="https://fonts.googleapis.com/css2?family=Lato:wght@400;700;900&family=Roboto+Condensed:wght@700&display=swap">
<style>
  :root{
    --green:#9bcb3c;
    --green-deep:#7fb52a;
    --blue:#0355a3;
    --blue-deep:#023f7d;
    --navy:#0c2f5c;
    --grey:#959595;
    --ink:#2a2a2a;
    --paper:#ffffff;
    --paper-shade:#e9ecef;
    --stage:#e4e4e4;
  }
  *{box-sizing:border-box;margin:0;padding:0}
  html,body{width:1200px;height:875px;overflow:hidden;background:var(--stage)}
  body{font-family:'Lato',Arial,sans-serif;color:var(--ink)}
  .brochure{position:absolute;left:30px;top:30px;width:1140px;height:814px;display:flex;box-shadow:0 6px 18px rgba(0,0,0,.25)}
  .panel{position:relative;width:380px;height:814px;overflow:hidden}
  .panel-bg{position:absolute;inset:0}
  .abs{position:absolute}

  .tab{position:absolute;height:34px;padding:0 28px 0 22px;background:var(--green);color:#fff;
       font:700 20px/34px 'Roboto Condensed',Arial,sans-serif;letter-spacing:.3px;
       clip-path:polygon(0 0,calc(100% - 16px) 0,100% 50%,calc(100% - 16px) 100%,0 100%)}

  /* About panel */
  .about-title{left:20px;top:102px;width:345px;font:700 12.5px/1.2 'Roboto Condensed',Arial,sans-serif;color:var(--ink);text-transform:uppercase}
  .about-body{left:20px;top:126px;width:345px;font-size:10.4px;line-height:13.2px;text-align:justify;color:#333}
  .about-body p{margin-bottom:12px}
  .about-photo{left:0;top:540px;width:180px;height:274px}
  .closing{right:14px;top:570px;width:215px;text-align:right}
  .closing h3{font:900 17.5px/1.35 'Lato',Arial,sans-serif;color:var(--ink);margin-bottom:8px}
  .closing p{margin-left:auto;width:160px;font:700 14.8px/19.2px 'Lato',Arial,sans-serif;color:#fff}

  /* Promise panel */
  .promise-text{left:20px;top:88px;width:340px;text-align:center;color:#fff;font-size:14.5px;line-height:23px}
  .brand{display:flex;align-items:center;justify-content:center;gap:10px;color:var(--grey);
         font:400 26px/1 'Lato',Arial,sans-serif;letter-spacing:.2px;white-space:nowrap}
  .brand-mark{width:14px;height:14px;background:var(--green);flex:none}
  .brand.small{font-size:23px}
  .office-brand{left:0;width:380px;top:318px}
  .office-title{left:0;width:380px;top:390px;text-align:center;color:#fff;font:700 21px/1 'Roboto Condensed',Arial,sans-serif}
  .contact{left:78px;width:290px;color:var(--blue-deep);font:700 16px/22px 'Lato',Arial,sans-serif;display:flex;gap:8px}
  .contact svg{flex:none;margin-top:3px}
  .map{left:79px;top:520px;width:218px;height:218px}
  .site{left:0;width:380px;top:768px;text-align:center;color:#fff;font:900 22px/1 'Lato',Arial,sans-serif;letter-spacing:.4px}

  /* Cover panel */
  .cover-brand{left:0;width:380px;top:95px}
  .headline{left:0;width:380px;top:184px;text-align:center;font:700 33px/42px 'Lato',Arial,sans-serif}
  .headline .line-blue{color:var(--blue);display:block}
  .headline .line-green{color:var(--green-deep);display:block}
  .cover-photo{left:0;top:300px;width:380px;height:400px}
  .cta{left:0;width:380px;top:726px;text-align:center}
  .cta .label{color:#fff;font:900 24px/1 'Lato',Arial,sans-serif;margin-bottom:10px}
  .cta .phone{color:var(--blue);font:900 30px/1 'Lato',Arial,sans-serif}
</style>
</head>
<body>
<main class="brochure">

  <!-- Panel: About -->
  <section class="panel panel-about">
    <svg class="panel-bg" width="380" height="814" viewBox="0 0 380 814" aria-hidden="true">
      <defs>
        <linearGradient id="aboutPaper" x1="0" y1="0" x2="1" y2="0">
          <stop offset="0" stop-color="var(--paper-shade)"/><stop offset=".5" stop-color="#fff"/><stop offset="1" stop-color="#f1f3f5"/>
        </linearGradient>
        <linearGradient id="aboutGreen" x1="0" y1="0" x2="0" y2="1">
          <stop offset="0" stop-color="#a9d445"/><stop offset="1" stop-color="#7fb52a"/>
        </linearGradient>
      </defs>
      <rect width="380" height="814" fill="url(#aboutPaper)"/>
      <rect width="380" height="10" fill="var(--navy)"/>
      <path d="M0 540 Q160 500 380 512 L380 530 Q170 518 0 558Z" fill="var(--blue)"/>
      <path d="M0 556 Q170 516 380 528 L380 814 L0 814Z" fill="url(#aboutGreen)"/>
    </svg>

    <div class="tab" style="left:0;top:40px">ABOUT US</div>
    <h2 class="abs about-title">Welcome to the practice of Maple Grin Family Dental</h2>
    <div class="abs about-body">
      <p>At Maple Grin Family Dental, we care about our patients. Our doctors and team want to help every patient achieve a healthy, beautiful smile that transcends the boundaries of their expectations and gives them a renewed sense of self-confidence. Here at Maple Grin Family Dental, we work hard to give our patients the personal attention they deserve, and our patients can always count on receiving the best care for themselves and their family.</p>
      <p>Here are a few reasons why Maple Grin Family Dental is a unique practice, for unique individuals:</p>
      <p>Dr. Ken Hollis and his team genuinely care about their patients! They strive to treat every patient as they themselves would expect to be treated. They even remember their patients' names! Doesn't it feel nice to be remembered? We think so!</p>
      <p>We don't just "clean teeth;" Dr. Hollis is also a certified Glimorel invisible braces provider, giving patients cleaner, healthier, and straighter smiles!</p>
      <p>Our practice offers our patients treatments for everything having to do with your teeth, mouth, gums, and jaw.</p>
      <p>The doctors and team at Maple Grin Family Dental are committed to excellence. Through continuing education we are able to stay up-to-date with current industry technology and techniques. Patients can trust that the treatments they receive are going to give them the results they expect for the smile they've always wanted.</p>
    </div>

    <div class="abs about-photo" role="img" aria-label="Photo of a smiling young woman in a scarf giving a thumbs up"
         style="background:linear-gradient(160deg,#e9d8c8 0%,#c9a58a 45%,#6b6560 100%)"></div>

    <div class="abs closing">
      <h3>We hope to see you and your smile soon!</h3>
      <p>Please contact our Edmonton dental practice to schedule an appointment today, and find out what it's like to work with a dental team committed to serving you!</p>
    </div>
  </section>

  <!-- Panel: Promise / Office -->
  <section class="panel panel-promise">
    <svg class="panel-bg" width="380" height="814" viewBox="0 0 380 814" aria-hidden="true">
      <defs>
        <linearGradient id="promiseBlue" x1="0" y1="0" x2="1" y2="0">
          <stop offset="0" stop-color="var(--blue-deep)"/><stop offset=".5" stop-color="#1673c4"/><stop offset="1" stop-color="var(--blue-deep)"/>
        </linearGradient>
        <radialGradient id="promiseGreen" cx=".5" cy=".45" r=".7">
          <stop offset="0" stop-color="#b6dc55"/><stop offset="1" stop-color="#7fb52a"/>
        </radialGradient>
      </defs>
      <rect width="380" height="814" fill="url(#promiseBlue)"/>
      <rect width="380" height="10" fill="var(--navy)"/>
      <path d="M0 262 Q150 220 380 244 L380 258 Q160 236 0 278Z" fill="#fff" opacity=".85"/>
      <path d="M0 276 Q160 236 380 256 L380 735 Q190 712 0 745Z" fill="url(#promiseGreen)"/>
    </svg>

    <div class="tab" style="left:0;top:36px">WE PROMISE</div>
    <p class="abs promise-text">Our team is committed to your total family dental health care! We offer complete and gentle dental care, and are committed to excellence in all that we do. Our warm and inviting office will provide a relaxed experience for your entire family.</p>

    <div class="abs brand small office-brand"><span class="brand-mark"></span>Maple Grin Family Dental</div>
    <h3 class="abs office-title">EDMONTON DENTAL OFFICE</h3>

    <div class="abs contact" style="top:428px">
      <svg width="16" height="16" viewBox="0 0 16 16" aria-hidden="true"><circle cx="8" cy="8" r="8" fill="var(--blue-deep)"/><path d="M8 3.5 3.5 7.5H5V12h2.2V9.5h1.6V12H11V7.5h1.5Z" fill="#fff"/></svg>
      <span>2150 - 98 Avenue NW<br>Edmonton, AB T5K 2J1</span>
    </div>
    <div class="abs contact" style="top:480px">
      <svg width="16" height="16" viewBox="0 0 16 16" aria-hidden="true"><rect width="16" height="16" rx="3" fill="var(--blue-deep)"/><rect x="5" y="3" width="6" height="10" rx="1" fill="#fff"/><rect x="6" y="4.5" width="4" height="5" fill="var(--blue-deep)"/></svg>
      <span>(780) 555-0142</span>
    </div>

    <svg class="abs map" viewBox="0 0 218 218" aria-hidden="true">
      <g transform="rotate(45 109 109)">
        <rect x="33" y="33" width="152" height="152" rx="14" fill="#fff"/>
      </g>
    </svg>
    <div class="abs" role="img" aria-label="Street map showing the office location with a location pin"
         style="left:113px;top:554px;width:150px;height:150px;transform:rotate(45deg);border-radius:10px;background:linear-gradient(135deg,#ecebe7,#dcdad4)"></div>

    <div class="abs site">WWW.MAPLEGRIN.CA</div>
  </section>

  <!-- Panel: Cover -->
  <section class="panel panel-cover">
    <svg class="panel-bg" width="380" height="814" viewBox="0 0 380 814" aria-hidden="true">
      <defs>
        <linearGradient id="coverPaper" x1="0" y1="0" x2="0" y2="1">
          <stop offset="0" stop-color="#f4f5f6"/><stop offset="1" stop-color="#fff"/>
        </linearGradient>
        <linearGradient id="coverGreen" x1="0" y1="0" x2="0" y2="1">
          <stop offset="0" stop-color="#a9d445"/><stop offset="1" stop-color="#86bb2e"/>
        </linearGradient>
      </defs>
      <rect width="380" height="814" fill="url(#coverPaper)"/>
      <rect width="380" height="10" fill="var(--navy)"/>
    </svg>

    <div class="abs cover-photo" role="img" aria-label="Photo of a smiling mother holding her laughing baby"
         style="background:linear-gradient(120deg,#f3ece6 0%,#e6cdb8 45%,#b98e70 75%,#e9e2dc 100%)"></div>

    <svg class="abs" style="left:0;top:0" width="380" height="814" viewBox="0 0 380 814" aria-hidden="true">
      <path d="M0 268 Q200 340 380 300 L380 310 Q200 352 0 290Z" fill="var(--green)"/>
      <path d="M0 262 Q200 336 380 296 L380 300 Q200 340 0 268Z" fill="var(--blue)"/>
      <path d="M0 10 H380 V296 Q200 336 0 262Z" fill="url(#coverPaper)"/>
      <path d="M0 690 Q180 655 380 672 L380 680 Q180 664 0 700Z" fill="var(--blue)"/>
      <path d="M0 700 Q180 664 380 680 L380 814 L0 814Z" fill="url(#coverGreen)"/>
    </svg>

    <div class="abs brand cover-brand"><span class="brand-mark"></span>Maple Grin Family Dental</div>
    <h1 class="abs headline"><span class="line-blue">YOUR YOUTHFUL</span><span class="line-green">SMILE IS FOR LIFE</span></h1>

    <div class="abs cta">
      <p class="label">CALL US TODAY!</p>
      <p class="phone">780-555-0142</p>
    </div>
  </section>

</main>
</body>
</html>
```